female esthetician looking for an impact business card

I an an expert in skin care industry with high experience in NYC.I want my business card to look professional , an impact at first look. I do want a combination between white and gold . I believe the font will be great if is gold.. The Fonts are also important. MARISELA VONDRAKE (SKIN CARE BOUTIQUE)

THIS SHOULD BE THE BUSINESS NAME, and should be placed on th eback of the card.
IN front m, the name MARISELA VONDRAKE - ESTHETCIAN

BY APPOINTMENTS ONLY: 555.218.9031

Target Market(s)

HIGH END CLIENTELE

Contact Information for Business Card

iT WILL BE on a luxury paper. I neeed the wow feeling

Requirements
Should not have
• pictures

```html
<!DOCTYPE html>
<html lang="en">
<head>
<meta charset="UTF-8">
<title>Marisela Vondrake – Skin Care Boutique Business Card</title>
<link href="https://fonts.googleapis.com/css2?family=Questrial&display=swap" rel="stylesheet">
<style>
  :root {
    --backdrop: #ece8e1;
    --card: #ffffff;
    --gold: #a97b2c;
    --gold-deep: #8f6a2c;
    --gold-line: #a9823c;
  }
  * { margin: 0; padding: 0; box-sizing: border-box; }
  html, body {
    width: 1200px;
    height: 902px;
    overflow: hidden;
    background: var(--backdrop);
  }
  .canvas {
    position: relative;
    width: 1200px;
    height: 902px;
  }
  .business-card {
    position: absolute;
    left: 100px;
    top: 165px;
    width: 1000px;
    height: 572px;
    background: var(--card);
    border-radius: 34px;
    box-shadow: 0 6px 22px rgba(60, 45, 20, 0.12);
    font-family: "Questrial", sans-serif;
    color: var(--gold);
  }
  .brand {
    position: absolute;
    left: 222px;
    top: 218px;
    display: flex;
    align-items: center;
    gap: 40px;
  }
  .brand-dot {
    width: 64px;
    height: 64px;
    border-radius: 50%;
    background: var(--gold);
    flex: none;
  }
  .brand-text {
    display: flex;
    flex-direction: column;
    align-items: flex-end;
  }
  .brand-name {
    font-size: 50px;
    font-weight: 400;
    letter-spacing: 1px;
    line-height: 1;
    white-space: nowrap;
  }
  .brand-tagline {
    display: flex;
    align-items: center;
    gap: 12px;
    margin-top: 8px;
    width: 100%;
  }
  .brand-tagline::before {
    content: "";
    flex: 1;
    height: 1.5px;
    background: var(--gold-line);
  }
  .brand-tagline span {
    font-size: 17px;
    letter-spacing: 2.5px;
    white-space: nowrap;
  }
  .appointments {
    position: absolute;
    left: 0;
    right: 0;
    top: 386px;
    text-align: center;
    font-size: 23px;
    letter-spacing: 4.5px;
    color: var(--gold-deep);
  }
  .phone-rule {
    position: absolute;
    left: 0;
    right: 0;
    top: 426px;
    display: flex;
    align-items: center;
    gap: 20px;
  }
  .phone-rule::before,
  .phone-rule::after {
    content: "";
    flex: 1;
    height: 2px;
    background: var(--gold-line);
  }
  .phone {
    font-size: 23px;
    letter-spacing: 1px;
    color: var(--gold-deep);
  }
</style>
</head>
<body>
  <main class="canvas">
    <section class="business-card">
      <div class="brand">
        <div class="brand-dot"></div>
        <div class="brand-text">
          <h1 class="brand-name">Marisela Vondrake</h1>
          <div class="brand-tagline"><span>SKIN CARE BOUTIQUE</span></div>
        </div>
      </div>
      <p class="appointments">BY APPOINTMENTS ONLY</p>
      <div class="phone-rule"><span class="phone">555.218.9031</span></div>
    </section>
  </main>
</body>
</html>
```